TFS Business Cards that rock.

New company needs business cards. We are a sports company that writes apps for golf. Company business cards should reflect our fun outgoing attitude but they are not to be "cartoonie".

On the back, we would like to use the plume app shelf icon and also be able to include a QR code so that our product is easy to find.

I have included a couple images and our company logo to be used as inspiration and incorporated as you see fit.

Target Market(s)

sports, golfers

Industry/Entity Type

Golf Course

Font styles to use
Serif
Sans Serif

Requirements
Must have
• Standard business info, no office phone, but mobile phone
• Company name is "Tall Fern Swing"
Nice to have
• Our tag line is:
• Connect
• You're In
• Let's Play!

```html
<!DOCTYPE html>
<html lang="en">
<head>
<meta charset="utf-8">
<title>Tall Fern Swing – Business Cards</title>
<link rel="stylesheet" href="https://fonts.googleapis.com/css2?family=Montserrat:wght@400;500;600&display=swap">
<style>
  :root {
    --stage: #e9ecef;
    --card-white: #ffffff;
    --brand-blue: #1f7fcf;
    --brand-sky: #2e9fe0;
    --brand-green: #5cbf3a;
    --ink: #2a2f36;
    --sky-top: #4a78c8;
    --sky-mid: #b9cde6;
    --grass: #4f8a2c;
    --grass-dark: #2f5a1c;
  }
  * { box-sizing: border-box; margin: 0; padding: 0; }
  html, body { width: 1200px; height: 852px; overflow: hidden; }
  body {
    background: var(--stage);
    font-family: "Montserrat", Arial, sans-serif;
    position: relative;
  }
  .card {
    position: absolute;
    width: 540px;
    height: 310px;
    border-radius: 18px;
    overflow: hidden;
    box-shadow: 0 10px 28px rgba(0,0,0,.18);
  }
  /* Front */
  .card-front { left: 50px; top: 130px; }
  .front-photo {
    position: absolute; inset: 0;
    background: linear-gradient(180deg, var(--sky-top) 0%, var(--sky-mid) 38%, #dfe6ea 46%, var(--grass) 58%, var(--grass-dark) 100%);
  }
  .front-title {
    position: absolute; top: 48px; left: 0; right: 0;
    text-align: center;
    color: #fff;
    font-size: 44px; font-weight: 500; letter-spacing: 2px;
  }
  /* Back */
  .card-back { left: 610px; top: 400px; background: var(--card-white); }
  .brand {
    position: absolute; left: 70px; top: 92px;
    display: flex; flex-direction: column; align-items: center; gap: 10px;
  }
  .brand-square { width: 96px; height: 96px; background: var(--brand-sky); }
  .brand-name { color: var(--brand-blue); font-size: 15px; font-weight: 600; letter-spacing: .5px; }
  .contact { position: absolute; left: 300px; top: 50px; color: var(--ink); }
  .person-name { font-size: 22px; font-weight: 500; letter-spacing: 1px; color: var(--brand-blue); }
  .person-name .last { color: var(--brand-green); }
  .person-role { font-size: 13px; margin-bottom: 6px; }
  .address { font-size: 13px; line-height: 1.4; margin-bottom: 6px; }
  .lines { list-style: none; font-size: 13px; line-height: 1.55; }
  .lines li { display: flex; align-items: center; gap: 8px; }
  .lines svg { width: 10px; height: 10px; fill: var(--brand-blue); }
  .band-line { position: absolute; left: 0; right: 0; bottom: 44px; height: 2px; background: var(--brand-green); }
  .band {
    position: absolute; left: 0; right: 0; bottom: 0; height: 40px;
    background: linear-gradient(90deg, var(--brand-sky), var(--brand-blue));
    color: #fff; font-size: 14px; letter-spacing: .5px;
    display: flex; align-items: center; justify-content: center;
  }
</style>
</head>
<body>
  <section class="card card-front">
    <div class="front-photo" role="img" aria-label="Golf course photo: seaside fairway with trees, winding cart path and bright sky"></div>
    <h1 class="front-title">TALL FERN SWING</h1>
  </section>

  <section class="card card-back">
    <div class="brand">
      <div class="brand-square"></div>
      <span class="brand-name">TALL FERN SWING</span>
    </div>
    <div class="contact">
      <p class="person-name">LUKAS <span class="last">BERNDT</span></p>
      <p class="person-role">Managing Partner</p>
      <p class="address">Lindenweg 12, 40210<br>Feldau, Germany</p>
      <ul class="lines">
        <li><svg viewBox="0 0 10 10"><path d="M2 0h2l1 3-1.5 1a6 6 0 0 0 2.5 2.5L7 5l3 1v2c0 1-1 2-2 2A8 8 0 0 1 0 2c0-1 1-2 2-2z"/></svg>+49 170 284 617 02</li>
        <li><svg viewBox="0 0 10 10"><path d="M0 2h10v6H0zM1 3l4 3 4-3" stroke="#fff" stroke-width=".8"/></svg>info@tallfernswing.com</li>
        <li><svg viewBox="0 0 10 10"><circle cx="5" cy="5" r="5"/><path d="M0 5h10M5 0v10" stroke="#fff" stroke-width=".7"/></svg>www.tallfernswing.com</li>
      </ul>
    </div>
    <div class="band-line"></div>
    <div class="band">The fighting game for real fighters.</div>
  </section>
</body>
</html>
```